Ridgely Forge business card for handing simple contact information and generating service awareness

Utilizing the attached logo(s), generate a professional, but approachable, card conveying a sense of capability and integrity. Please only use one logo of the four attached; the different colors are all acceptable, but preference will be given to a design integrating a teal/turquoise logo,

I do not know where to put in the contact information or details?

Target Market(s)

Agriculture, Farming, Timber, Forestry, Construction, Crane Service

Industry/Entity Type

Contact Information for Business Card

Name, Phone Number, email address

Colors

Designer to choose colors to be used in the design.

Requirements
Nice to have
• It would be great to have either a mountain or one of the attached cranes as a backdrop on the rear of the card. Simple watermarks and/or Debossing is also great

```html
<!DOCTYPE html>
<html lang="en">
<head>
<meta charset="utf-8">
<title>Ridgely Forge Business Card</title>
<link href="https://fonts.googleapis.com/css2?family=Montserrat:wght@400;500;800&display=swap" rel="stylesheet">
<style>
  :root {
    --teal: #2a6f62;
    --teal-deep: #246457;
    --teal-soft: #34796c;
    --ink: #2e2e2e;
    --paper: #ffffff;
    --backdrop: #bdbdbd;
    --divider: #6f9c92;
  }
  * { margin: 0; padding: 0; box-sizing: border-box; }
  html, body { width: 1200px; height: 802px; overflow: hidden; }
  body {
    background: var(--backdrop);
    font-family: "Montserrat", sans-serif;
    position: relative;
  }
  .card {
    position: absolute;
    top: 246px;
    width: 540px;
    height: 310px;
    border-radius: 22px;
    overflow: hidden;
  }
  .card--front { left: 40px; background: var(--paper); }
  .card--back { left: 620px; background: var(--teal); }

  /* front */
  .brand-mark {
    position: absolute;
    left: 48px; top: 52px;
    width: 200px;
    text-align: center;
    font-weight: 800;
    font-size: 26px;
    letter-spacing: 1px;
    color: var(--teal);
    text-transform: uppercase;
  }
  .person {
    position: absolute;
    left: 48px; top: 150px;
    width: 200px;
    text-align: right;
  }
  .person__name {
    font-weight: 800;
    font-size: 21px;
    letter-spacing: 1px;
    color: var(--teal);
    text-transform: uppercase;
  }
  .person__title {
    font-size: 14px;
    color: var(--ink);
    margin-top: 2px;
  }
  .divider {
    position: absolute;
    left: 272px; top: 140px;
    width: 1.5px; height: 62px;
    background: var(--divider);
  }
  .contacts {
    position: absolute;
    left: 292px; top: 48px;
    list-style: none;
    font-size: 14px;
    color: var(--ink);
  }
  .contacts li { display: flex; align-items: center; gap: 7px; height: 27px; }
  .contacts svg { width: 12px; height: 12px; fill: var(--teal); flex: none; }
  .address {
    position: absolute;
    left: 48px; right: 40px; bottom: 44px;
    font-size: 14.5px;
    color: var(--ink);
    text-align: center;
  }

  /* back */
  .backdrop-art {
    position: absolute; inset: 0;
    background: radial-gradient(ellipse at 70% 40%, var(--teal-soft) 0%, var(--teal) 55%, var(--teal-deep) 100%);
  }
  .back-brand {
    position: absolute;
    left: 0; right: 0; top: 130px;
    display: flex; justify-content: center; align-items: center; gap: 14px;
  }
  .back-brand__dot {
    width: 26px; height: 26px; border-radius: 50%;
    background: var(--paper);
  }
  .back-brand__name {
    font-weight: 800;
    font-size: 36px;
    letter-spacing: 1.5px;
    color: var(--paper);
    text-transform: uppercase;
  }
</style>
</head>
<body>
  <section class="card card--front">
    <div class="brand-mark">Ridgely Forge</div>
    <div class="person">
      <p class="person__name">Corin Maddox</p>
      <p class="person__title">CEO/Founder</p>
    </div>
    <div class="divider"></div>
    <ul class="contacts">
      <li><svg viewBox="0 0 24 24"><path d="M6.6 10.8a15.1 15.1 0 0 0 6.6 6.6l2.2-2.2c.3-.3.7-.4 1-.2 1.1.4 2.3.6 3.6.6.6 0 1 .4 1 1V20c0 .6-.4 1-1 1A17 17 0 0 1 3 4c0-.6.4-1 1-1h3.5c.6 0 1 .4 1 1 0 1.3.2 2.5.6 3.6.1.3 0 .7-.2 1z"/></svg>123-555-01842</li>
      <li><svg viewBox="0 0 24 24"><path d="M7 1h10a2 2 0 0 1 2 2v18a2 2 0 0 1-2 2H7a2 2 0 0 1-2-2V3a2 2 0 0 1 2-2zm0 4v13h10V5z"/></svg>126-555-01937</li>
      <li><svg viewBox="0 0 24 24"><path d="M2 5h20v14H2zm2 2v.5l8 5 8-5V7z"/></svg>info@ridgelyforge.com</li>
      <li><svg viewBox="0 0 24 24"><circle cx="12" cy="12" r="10"/></svg>www.ridgelyforge.com</li>
    </ul>
    <p class="address">88 Alder Row, 3rd Floor Pine Hollow, AB 85730</p>
  </section>

  <section class="card card--back">
    <div class="backdrop-art" role="img" aria-label="Faint tonal backdrop of pine forest and mountain scenery"></div>
    <div class="back-brand">
      <span class="back-brand__dot"></span>
      <span class="back-brand__name">Ridgely Forge</span>
    </div>
  </section>
</body>
</html>
```